Business Card Design

I am an Event and Wedding Planner in need of an eye catching business card featuring my logo (attached), my contact details, and my company tagline (Making each one of your gatherings radiant...) I would like the tagline in font similar the logo's font.
Updates
I have just noticed that my logo has a misspelling so for the final design, I will be uploading a corrected logo as soon as I have it.
My apologies.
Reason: Waiting on a corrected logo...Occasions is misspelled and it should say Weddings not Wedding
The logo has been corrected so now Occasions is spelled correctly and it says Weddings instead of Wedding. Please use Edwardian Script ITC as the font for the tagline so it will match the logo. Thank you for your patience.
Target Market(s)
Engaged couples and people hosting milestone celebrations. 25-50 years old, predominately female
Industry/Entity Type
Business
Contact Information for Business Card
Delphine Marsh, Event Manager / Owner, Mobile: 0491 836 254, Email: delphine@radiantgatheringsco.com.au, www.radiantgatheringsco.com.au, Making each one of your gatherings radiant...

```html
<!DOCTYPE html>
<html lang="en">
<head>
<meta charset="utf-8">
<title>Radiant Gatherings Co. — Business Card</title>
<link href="https://fonts.googleapis.com/css2?family=Open+Sans:wght@400;600&family=Pinyon+Script&display=swap" rel="stylesheet">
<style>
  :root {
    --backdrop: #e4e2df;
    --card: #ffffff;
    --ink: #2a2a2a;
    --band: #1f1d1e;
    --band-text: #d9d6d3;
    --accent: #c8262c;
    --muted: #5a5a5a;
    --rule: #9a9a9a;
  }
  * { box-sizing: border-box; margin: 0; padding: 0; }
  html, body {
    width: 1200px; height: 872px; overflow: hidden;
    background: var(--backdrop);
    font-family: "Open Sans", Arial, sans-serif;
    color: var(--ink);
  }
  .sheet {
    width: 1200px; height: 872px;
    display: flex; align-items: center; justify-content: center; gap: 60px;
  }
  .card {
    position: relative;
    width: 525px; height: 300px;
    background: var(--card);
    box-shadow: 0 6px 18px rgba(0,0,0,.18);
    overflow: hidden;
  }
  /* Front */
  .tagline-band {
    position: absolute; left: 0; top: 0; width: 100%; height: 62px;
    background: var(--band);
    display: flex; align-items: center; justify-content: center;
  }
  .tagline {
    font-family: "Pinyon Script", cursive;
    font-size: 25px; color: var(--band-text);
  }
  .contact-list {
    position: absolute; left: 34px; top: 86px;
    list-style: none; display: flex; flex-direction: column; gap: 9px;
  }
  .contact-item {
    display: flex; align-items: center; gap: 10px;
    font-size: 12.5px; color: var(--ink);
  }
  .contact-icon { width: 20px; height: 20px; flex: none; }
  .holder { position: absolute; left: 34px; bottom: 34px; }
  .holder-name { font-size: 23px; font-weight: 400; letter-spacing: .2px; }
  .holder-role { font-size: 14px; color: var(--accent); margin-top: 2px; }
  .brand-front {
    position: absolute; right: 30px; bottom: 40px;
    display: flex; align-items: center; gap: 8px;
  }
  .brand-name {
    font-family: "Open Sans", Arial, sans-serif;
    font-weight: 600; color: var(--ink);
  }
  .brand-front .brand-name { font-size: 17px; }
  .brand-dot { border-radius: 50%; background: var(--accent); flex: none; }
  .brand-front .brand-dot { width: 12px; height: 12px; }
  /* Back */
  .card-back { display: flex; align-items: center; justify-content: center; }
  .brand-back { display: flex; align-items: center; gap: 14px; }
  .brand-back .brand-name { font-size: 30px; }
  .brand-back .brand-dot { width: 20px; height: 20px; }
</style>
</head>
<body>
<main class="sheet">
  <section class="card card-front" aria-label="Business card front">
    <div class="tagline-band">
      <p class="tagline">Making each one of your gatherings radiant...</p>
    </div>

    <ul class="contact-list">
      <li class="contact-item">
        <svg class="contact-icon" viewBox="0 0 20 20" aria-hidden="true">
          <circle cx="10" cy="10" r="10" fill="#2a2a2a"/>
          <circle cx="10" cy="10" r="5.5" fill="none" stroke="#fff" stroke-width="1.2"/>
          <path d="M4.5 10h11M10 4.5c-2.5 3-2.5 8 0 11M10 4.5c2.5 3 2.5 8 0 11" fill="none" stroke="#fff" stroke-width="1"/>
        </svg>
        <span>www.radiantgatheringsco.com.au</span>
      </li>
      <li class="contact-item">
        <svg class="contact-icon" viewBox="0 0 20 20" aria-hidden="true">
          <circle cx="10" cy="10" r="10" fill="#2a2a2a"/>
          <rect x="5" y="6.5" width="10" height="7" fill="none" stroke="#fff" stroke-width="1.2"/>
          <path d="M5 6.5l5 4 5-4" fill="none" stroke="#fff" stroke-width="1.2"/>
        </svg>
        <span>delphine@radiantgatheringsco.com.au</span>
      </li>
      <li class="contact-item">
        <svg class="contact-icon" viewBox="0 0 20 20" aria-hidden="true">
          <circle cx="10" cy="10" r="10" fill="#2a2a2a"/>
          <path d="M7 5.5l2 2.2-1.1 1.4c.7 1.4 1.6 2.3 3 3l1.4-1.1 2.2 2-1.2 1.6c-3.6-.4-6.8-3.6-7.2-7.2z" fill="#fff"/>
        </svg>
        <span>0491 836 254</span>
      </li>
    </ul>

    <div class="holder">
      <h1 class="holder-name">Delphine Marsh</h1>
      <p class="holder-role">Event Manager / Owner</p>
    </div>

    <div class="brand-front">
      <span class="brand-name">Radiant Gatherings Co.</span>
      <span class="brand-dot"></span>
    </div>
  </section>

  <section class="card card-back" aria-label="Business card back">
    <div class="brand-back">
      <span class="brand-name">Radiant Gatherings Co.</span>
      <span class="brand-dot"></span>
    </div>
  </section>
</main>
</body>
</html>
```